New Web Design Project

Require a website for The Marrow Orchard. All relevant information is in the uploaded files.

website to be responsive to work on mobile.

Required in html5, css

Coding

Coded - Design and coding required

Number of Pages Required

3 page

```html
<!DOCTYPE html>
<html lang="en">
<head>
<meta charset="utf-8">
<title>The Marrow Orchard</title>
<link href="https://fonts.googleapis.com/css2?family=Rubik:wght@500;700&family=Roboto:ital,wght@0,400;0,500;0,700;1,400&display=swap" rel="stylesheet">
<style>
:root{
  --green:#6cb52d;
  --orange:#f08a1d;
  --dark:#333538;
  --text:#555;
  --head:#2e2e2e;
  --grey:#f2f2f3;
}
*{box-sizing:border-box;margin:0;padding:0}
html,body{width:1200px;height:4304px;overflow:hidden;background:#fff}
body{font-family:"Roboto",sans-serif;color:var(--text)}
.page{position:relative;width:1200px;height:4304px;overflow:hidden}
.abs{position:absolute}
h1,h2,h3{font-family:"Rubik",sans-serif;color:var(--head)}
.section-title{position:absolute;left:0;width:1200px;text-align:center;font-size:46px;font-weight:700}

/* header */
.topline{top:0;left:0;width:1200px;height:5px;background:var(--green)}
.header{top:5px;left:0;width:1200px;height:92px;background:#fff;z-index:3}
.nav a{position:absolute;top:38px;font-size:15px;font-weight:500;color:#222;text-decoration:none}
.nav a.active{color:var(--green)}
.brand-badge{left:505px;top:20px;width:190px;height:132px;border-radius:0 0 95px 95px;background:#fff;z-index:4;text-align:center}
.brand-badge .dot{width:34px;height:34px;border-radius:50%;background:var(--orange);margin:8px auto 6px}
.brand-badge .name{font-family:"Rubik",sans-serif;font-weight:500;font-size:19px;color:#3a3a3a;line-height:1.1}
.search{left:930px;top:43px}
.login{left:980px;top:32px;width:108px;height:38px;border-radius:19px;background:var(--orange);color:#fff;font-size:15px;font-weight:500;text-align:center;line-height:38px}

/* hero */
.hero-photo{top:97px;left:0;width:1200px;height:650px;background:linear-gradient(180deg,#6d95c4 0%,#a9bfd6 40%,#8a97a4 62%,#50657a 78%,#2d4a63 100%)}
.hero-title{top:283px;left:0;width:1200px;text-align:center;color:#fff;font-size:57px;font-weight:700}
.hero-sub{top:365px;left:340px;width:520px;text-align:center;color:#fff;font-size:16px;line-height:27px}
.btn-start{top:449px;left:507px;width:186px;height:48px;border-radius:24px;background:var(--orange);color:#fff;font-weight:700;font-size:16px;text-align:center;line-height:48px}
.hero-arrow{top:368px;width:36px;height:36px;border:2px solid #fff;border-radius:50%}

/* about */
.about-mark{left:140px;top:800px;width:380px;height:480px;text-align:center}
.about-mark .circle{width:300px;height:300px;border-radius:50%;background:var(--orange);margin:40px auto 40px}
.about-mark .name{font-family:"Rubik",sans-serif;font-weight:500;font-size:34px;color:var(--green)}
.about-title{left:600px;top:848px;font-size:46px}
.about-text{left:600px;top:918px;width:490px;font-size:14px;line-height:25px}
.about-text p{margin-bottom:8px}
.about-link{left:600px;top:1219px;font-size:14.5px;font-weight:500;color:var(--green)}

/* services */
.card{top:1557px;width:312px;height:345px;background:#fff;box-shadow:0 2px 10px rgba(0,0,0,.06);text-align:center}
.card .photo{height:183px}
.card h3{font-family:"Roboto",sans-serif;font-size:18px;font-weight:700;margin-top:46px;color:#222}
.card p{font-size:13.5px;line-height:23px;margin:10px 22px 0}
.card.featured{background:var(--orange)}
.card.featured h3,.card.featured p{color:#fff}

/* team */
.member{top:2256px;width:478px;height:268px;border:3px solid var(--green);background:#fff}
.member .photo{position:absolute;left:8px;top:8px;width:188px;height:248px}
.member .info{position:absolute;left:222px;top:30px;width:240px}
.member h3{font-family:"Roboto",sans-serif;font-size:18px;font-weight:500;color:#222;border-left:3px solid var(--orange);padding-left:12px;line-height:20px}
.member .role{font-size:12px;color:#888;padding-left:15px;border-left:3px solid var(--orange);line-height:18px}
.member p{font-size:13.5px;line-height:24px;margin-top:18px;padding-left:2px}
.socials{margin-top:20px;display:flex;gap:10px}
.socials span{width:27px;height:27px;border-radius:50%;background:#eef1f6;display:block}

/* testimonial */
.quote-title{top:2832px;left:320px;font-size:34px;color:#fff;font-weight:700;letter-spacing:.5px}
.avatar{top:2894px;left:178px;width:108px;height:108px;transform:rotate(45deg);border:3px solid #fff;background:linear-gradient(135deg,#5ab0e0,#2f6fa8)}
.quote{top:2911px;left:321px;width:680px;color:#fff;font-style:italic;font-size:15px;line-height:27px}
.quote-name{top:3000px;left:321px;color:#fff;font-weight:500;font-size:17px}
.quote-co{top:3025px;left:321px;color:#fff;font-size:12px}
.t-arrow{top:2940px}

/* news */
.news-big{top:3300px;left:117px;width:451px;height:385px;background:linear-gradient(180deg,#c9a98a 0%,#9e7f66 55%,#6a7a55 100%)}
.news-big .overlay{position:absolute;left:110px;top:203px;width:341px;height:182px;background:rgba(240,138,29,.93);color:#fff;padding:24px 0 0 16px}
.news-big h3{font-family:"Roboto",sans-serif;color:#fff;font-size:18px;font-weight:500;line-height:24px;width:300px}
.meta{font-size:12.5px;margin-top:14px}
.meta-green{color:var(--green)}
.news-big p{font-size:13px;line-height:21px;margin-top:18px;width:310px}
.news-small{left:603px;width:480px;height:181px;border:1px solid #e4e4e4;background:#fff}
.news-small .photo{position:absolute;left:0;top:0;width:202px;height:179px}
.news-small .body{position:absolute;left:227px;top:20px;width:235px}
.news-small h3{font-family:"Roboto",sans-serif;font-size:16px;font-weight:500;color:#222}
.news-small p{font-size:13px;line-height:21px;margin-top:14px;color:#666}

/* footer */
.f-brand{left:110px;top:3977px;width:230px;text-align:center}
.f-brand .dot{width:62px;height:62px;border-radius:50%;background:var(--orange);margin:0 auto 18px}
.f-brand .name{font-family:"Rubik",sans-serif;font-weight:500;font-size:36px;color:#fff;line-height:40px}
.f-head{top:3962px;color:#fff;font-weight:700;font-size:16px}
.contact-item{left:388px;width:240px;color:#fff;font-size:12.5px;line-height:18px}
.contact-item .ic{position:absolute;left:0;top:0;width:36px;height:36px;border:2px solid #fff;border-radius:50%}
.contact-item .tx{position:absolute;left:56px;top:0;width:190px}
.field{background:#fff;color:#999;font-size:11.5px;padding:8px 12px;height:31px;border:1px solid #ddd}
.submit{left:668px;top:4184px;width:96px;height:30px;border-radius:15px;background:#e8262b;color:#fff;font-weight:700;font-size:13px;text-align:center;line-height:30px}
.f-rule{top:4244px;left:110px;width:980px;height:1px;background:#555}
.copy{top:4260px;left:110px;color:#fff;font-size:12.5px}
.f-social{top:4253px;left:940px;display:flex;gap:8px}
.f-social span{width:31px;height:31px;border-radius:50%;border:2px solid #fff;display:block}
</style>
</head>
<body>
<div class="page">

  <div class="abs hero-photo" role="img" aria-label="City skyline with a tall tower seen across the water"></div>
  <svg class="abs" style="left:0;top:600px" width="1200" height="170" viewBox="0 0 1200 170">
    <path d="M0 120 C200 40 420 40 600 100 C780 160 980 110 1200 50 L1200 170 L0 170Z" fill="var(--orange)"/>
    <path d="M0 135 C200 60 420 55 600 115 C780 170 980 130 1200 60 L1200 170 L0 170Z" fill="var(--green)"/>
    <path d="M0 160 C200 85 420 80 600 135 C780 185 980 150 1200 95 L1200 170 L0 170Z" fill="#fff"/>
  </svg>

  <h1 class="abs hero-title">The Marrow Orchard</h1>
  <p class="abs hero-sub">Lorem ipsum dolor sit amet, consectetur adipiscing elit, sed do eiusmod tempor incididunt ut labore et aliqua.</p>
  <div class="abs btn-start">GET STARTED &#10140;</div>
  <svg class="abs hero-arrow" style="left:35px" viewBox="0 0 36 36"><path d="M20 11 L13 18 L20 25" stroke="#fff" stroke-width="2.5" fill="none"/></svg>
  <svg class="abs hero-arrow" style="left:1125px" viewBox="0 0 36 36"><path d="M16 11 L23 18 L16 25" stroke="#fff" stroke-width="2.5" fill="none"/></svg>

  <div class="abs topline"></div>
  <div class="abs header">
    <nav class="nav">
      <a class="active" style="left:110px">Home</a>
      <a style="left:179px">About Us</a>
      <a style="left:269px">Our Services</a>
      <a style="left:383px">Team</a>
      <a style="left:763px">News</a>
      <a style="left:829px">Contact Us</a>
    </nav>
    <svg class="abs search" width="16" height="16" viewBox="0 0 16 16"><circle cx="6.5" cy="6.5" r="5" stroke="#222" stroke-width="2" fill="none"/><path d="M10 10 L15 15" stroke="#222" stroke-width="2.2"/></svg>
    <div class="abs login">&#9679; Login</div>
  </div>
  <div class="abs brand-badge">
    <div class="dot"></div>
    <div class="name">The Marrow<br>Orchard</div>
  </div>

  <div class="abs about-mark">
    <div class="circle"></div>
    <div class="name">The Marrow Orchard</div>
  </div>
  <h2 class="abs about-title">About Us</h2>
  <div class="abs about-text">
    <p>The Marrow Orchard was incorporated with the objective of introducing new vendors to the Canadian market through a trusted and mutual business relation</p>
    <p>It was set up by Idris Kalloway and Stavros Menidi who have a combined experience of over 45 years in the fresh produce business. With Idris's expertise in global sourcing and Stavros's vast connection and know how of the Canadian market, we have helped our existing partners grow and expand their reach in the Canadian fresh produce market.</p>
    <p>Our expertise and supply chain knowledge allow us to develop programs and introduce new products to the Canadian consumer, via retail and wholesale channels across Canada.</p>
  </div>
  <div class="abs about-link">Get in touch to discuss how we can add value to your business</div>

  <svg class="abs" style="left:0;top:1330px" width="1200" height="760" viewBox="0 0 1200 760">
    <path d="M0 20 C150 120 350 120 600 60 C850 0 1050 0 1200 40 L1200 640 C1050 640 950 620 800 650 C600 700 300 780 0 650Z" fill="var(--grey)"/>
    <path d="M0 20 C150 120 350 120 600 60 C700 35 760 28 800 26" stroke="var(--orange)" stroke-width="4" fill="none"/>
    <path d="M760 648 C900 620 1050 630 1200 725" stroke="var(--orange)" stroke-width="4" fill="none"/>
  </svg>
  <h2 class="section-title" style="top:1470px">Our Services</h2>
  <div class="abs card" style="left:110px">
    <div class="photo" role="img" aria-label="Shoppers buying fresh produce at a market stall" style="background:linear-gradient(160deg,#8aa67a,#c9906a)"></div>
    <h3>Lorem ipsum dolor sit amet</h3>
    <p>Lorem ipsum dolor sit amet, consectetur adipiscing elit, sed do eiusmod tempor incididunt ut labore et dolore</p>
  </div>
  <div class="abs card featured" style="left:444px">
    <div class="photo" role="img" aria-label="Baker holding fresh bread in a shop" style="background:linear-gradient(160deg,#6b4a35,#b07a4e)"></div>
    <h3>Lorem ipsum dolor sit amet</h3>
    <p>Lorem ipsum dolor sit amet, consectetur adipiscing elit, sed do eiusmod tempor incididunt ut labore et dolore</p>
  </div>
  <div class="abs card" style="left:777px">
    <div class="photo" role="img" aria-label="Business partners shaking hands in an office" style="background:linear-gradient(160deg,#8e959e,#3d434b)"></div>
    <h3>Lorem ipsum dolor sit amet</h3>
    <p>Lorem ipsum dolor sit amet, consectetur adipiscing elit, sed do eiusmod tempor incididunt ut labore et dolore</p>
  </div>

  <h2 class="section-title" style="top:2153px">Team People</h2>
  <div class="abs member" style="left:109px">
    <div class="photo" role="img" aria-label="Portrait of Idris Kalloway in a suit" style="background:linear-gradient(180deg,#d8d4cc,#3b3b40)"></div>
    <div class="info">
      <h3>Idris Kalloway</h3>
      <div class="role">Founder &amp; President</div>
      <p>Lorem ipsum dolor sit consectetur adipiscing elit, sed eiusmod tempor incididunt ut labore dolore magna minim veniam aliqua.</p>
      <div class="socials"><span></span><span></span><span></span><span></span></div>
    </div>
  </div>
  <div class="abs member" style="left:615px">
    <div class="photo" role="img" aria-label="Portrait of Stavros Menidi in a suit" style="background:linear-gradient(180deg,#bdb6ad,#2d3440)"></div>
    <div class="info">
      <h3>Stavros Menidi</h3>
      <div class="role">Founder</div>
      <p>Lorem ipsum dolor sit consectetur adipiscing elit, sed eiusmod tempor incididunt ut labore dolore magna minim veniam aliqua.</p>
      <div class="socials"><span></span><span></span><span></span><span></span></div>
    </div>
  </div>

  <svg class="abs" style="left:0;top:2630px" width="1200" height="560" viewBox="0 0 1200 560">
    <path d="M0 60 C200 150 420 90 650 40 C850 0 1050 20 1200 50 L1200 520 C1000 470 800 470 600 510 C400 550 200 560 0 470Z" fill="var(--orange)"/>
    <path d="M0 72 C200 160 420 100 650 52 C850 12 1050 32 1200 62 L1200 510 C1000 455 800 455 600 495 C400 535 200 545 0 460Z" fill="var(--green)"/>
  </svg>
  <h2 class="abs quote-title">WHAT OUR CLIENTS HAVE TO SAY</h2>
  <div class="abs avatar" role="img" aria-label="Client portrait"></div>
  <p class="abs quote">Lorem ipsum dolor sit amet, consectetur adipiscing elit, sed do eiusmod tempor incididunt ut labore et dolore magna aliqua. Ut enim ad minim veniam, quis nostrud exercitation ullamco laboris nisi ut aliquip ex ea commodo consequat.</p>
  <div class="abs quote-name">John Doe</div>
  <div class="abs quote-co">Company Name</div>
  <svg class="abs t-arrow" style="left:108px" width="24" height="40" viewBox="0 0 24 40"><path d="M20 4 L5 20 L20 36" stroke="#fff" stroke-width="4" fill="none"/></svg>
  <svg class="abs t-arrow" style="left:1064px" width="24" height="40" viewBox="0 0 24 40"><path d="M4 4 L19 20 L4 36" stroke="#fff" stroke-width="4" fill="none"/></svg>

  <h2 class="section-title" style="top:3213px">Recent News</h2>
  <div class="abs news-big" role="img" aria-label="Friends sharing a meal in a kitchen">
    <div class="overlay">
      <h3>Nemo enim ipsam voluptatem quia voluptas sit aspernatur</h3>
      <div class="meta">&#9632; Nov 05, 2020 &nbsp;|&nbsp; &#9679; 2 Comments</div>
      <p>Sed ut perspiciatis unde omnis iste natus error sit voluptatem accusantium doloremque</p>
    </div>
  </div>
  <div class="abs news-small" style="top:3300px">
    <div class="photo" role="img" aria-label="Customers buying vegetables at a grocery" style="background:linear-gradient(160deg,#9fb07a,#c7a77c)"></div>
    <div class="body">
      <h3>Nemo enim ipsam voluptatem</h3>
      <div class="meta meta-green">&#9632; Nov 05, 2020 &nbsp;|&nbsp; &#9679; 2 Comments</div>
      <p>Sed ut perspiciatis unde omnis iste natus voluptatem accusantium doloremque laudantium,</p>
    </div>
  </div>
  <div class="abs news-small" style="top:3504px">
    <div class="photo" role="img" aria-label="Shop worker carrying a crate of bottles" style="background:linear-gradient(160deg,#3a4f86,#b5553a)"></div>
    <div class="body">
      <h3>Nemo enim ipsam voluptatem</h3>
      <div class="meta meta-green">&#9632; Nov 05, 2020 &nbsp;|&nbsp; &#9679; 2 Comments</div>
      <p>Sed ut perspiciatis unde omnis iste natus voluptatem accusantium doloremque laudantium,</p>
    </div>
  </div>

  <svg class="abs" style="left:0;top:3770px" width="1200" height="534" viewBox="0 0 1200 534">
    <path d="M0 30 C200 110 350 100 600 40 C850 -10 1050 20 1200 90 L1200 534 L0 534Z" fill="var(--orange)"/>
    <path d="M0 45 C200 125 350 115 600 55 C850 5 1050 35 1200 105 L1200 534 L0 534Z" fill="var(--green)"/>
    <path d="M0 62 C200 140 350 132 600 72 C850 22 1050 55 1200 125 L1200 534 L0 534Z" fill="var(--dark)"/>
  </svg>
  <div class="abs f-brand">
    <div class="dot"></div>
    <div class="name">The Marrow<br>Orchard</div>
  </div>
  <div class="abs f-head" style="left:388px">CONTACT INFORMATION</div>
  <div class="abs contact-item" style="top:4004px">
    <svg class="ic" viewBox="0 0 36 36"><path d="M18 9 C14 9 12 12 12 15 C12 19 18 26 18 26 C18 26 24 19 24 15 C24 12 22 9 18 9Z" fill="#fff"/><circle cx="18" cy="15" r="2.4" fill="var(--dark)"/></svg>
    <div class="tx">123, Lorem ipsum dolor amet, consectetur adipiscing</div>
  </div>
  <div class="abs contact-item" style="top:4056px">
    <svg class="ic" viewBox="0 0 36 36"><path d="M12 11 L15 10 L17 15 L15 16.5 C16 19 17 20 19.5 21 L21 19 L26 21 L25 24 C18 25 11 18 12 11Z" fill="#fff"/></svg>
    <div class="tx">Phone :<br>+1 555 014 2290</div>
  </div>
  <div class="abs contact-item" style="top:4106px">
    <svg class="ic" viewBox="0 0 36 36"><rect x="10" y="12" width="16" height="12" fill="#fff"/><path d="M10 12 L18 19 L26 12" stroke="var(--dark)" stroke-width="1.6" fill="none"/></svg>
    <div class="tx">Email :<br>hello@marroworchard.com</div>
  </div>
  <div class="abs contact-item" style="top:4160px">
    <svg class="ic" viewBox="0 0 36 36"><rect x="12" y="10" width="12" height="16" fill="#fff"/><rect x="14.5" y="16" width="7" height="6" fill="var(--dark)"/></svg>
    <div class="tx">Fax :<br>555 014 7781</div>
  </div>

  <div class="abs f-head" style="left:667px">GET IN TOUCH:</div>
  <div class="abs field" style="left:668px;top:4010px;width:206px">Name :</div>
  <div class="abs field" style="left:882px;top:4010px;width:206px">Phone :</div>
  <div class="abs field" style="left:668px;top:4049px;width:420px">Email :</div>
  <div class="abs field" style="left:668px;top:4091px;width:420px;height:70px">Message :</div>
  <div class="abs submit">SUBMIT</div>

  <div class="abs f-rule"></div>
  <div class="abs copy">Copyrights &copy; 2020, The Marrow Orchard. All Rights Reserved. &nbsp;|&nbsp; Privacy policy</div>
  <div class="abs f-social"><span></span><span></span><span></span><span></span></div>

</div>
</body>
</html>
```